UI/ UX Design for ERP Software

We need a new UX/UI interface for a ERP software for property managers. Our CMMS / ERP solution is made based on responsive design technologies and is coded in PHP.
The overall UX to be similar to Tarn Vexa - easy navigation, intuitive menus.

Industry/Entity Type

Property Management

Number of Pages Required

5+ page

Requirements
Must have
• Round dock buttons
Consistent icons across the application
Enough Spacing between buttons/icons/ menu
Consistent Font
Nice to have
• We would like the UX to allow the users to use the application without /minimum training.
Should not have
• we don't want anything that is classic with respect to UX

```html
<!DOCTYPE html>
<html lang="en">
<head>
<meta charset="utf-8">
<title>Nestora — Property Dashboard</title>
<link href="https://fonts.googleapis.com/css2?family=Source+Sans+3:wght@400;600&display=swap" rel="stylesheet">
<style>
  :root {
    --page: #f3f6f7;
    --teal-light: #72c7c2;
    --teal: #5ea5aa;
    --teal-dark: #4a8799;
    --ink: #2f4a55;
    --ink-teal: #3e7f8f;
    --chip: #dce4e7;
    --panel: #e8edee;
    --line: #cfd8db;
    --white: #ffffff;
  }
  * { box-sizing: border-box; margin: 0; padding: 0; }
  html, body { width: 1200px; height: 831px; overflow: hidden; }
  body {
    background: var(--page);
    font-family: "Source Sans 3", sans-serif;
    color: var(--ink);
    position: relative;
  }
  .sidebar {
    position: absolute; left: 113px; top: 50px; width: 314px; height: 735px;
    border-radius: 22px;
    background: linear-gradient(180deg, var(--teal-light) 0%, var(--teal) 50%, var(--teal-dark) 100%);
  }
  .brand {
    position: absolute; left: 214px; top: 90px; width: 170px; height: 61px;
    background: rgba(255,255,255,0.35);
    display: flex; align-items: center; justify-content: center; gap: 8px;
    color: #3aa7b6; font-size: 22px; font-weight: 600;
  }
  .brand-mark { width: 14px; height: 14px; background: #3aa7b6; }
  .dock-btn {
    position: absolute; height: 80px; border-radius: 18px;
    display: flex; align-items: center; padding-left: 24px; gap: 22px;
    font-size: 17px; color: var(--white);
    border: 2px solid rgba(255,255,255,0.9);
    background: linear-gradient(90deg, var(--teal-light), var(--teal-dark));
    box-shadow: 10px 10px 26px rgba(74,135,153,0.35);
  }
  .dock-btn svg { width: 40px; height: 28px; flex: none; }
  .dock-btn.no-icon { padding-left: 90px; }
  .dock-btn.active {
    background: rgba(235,241,243,0.92); color: var(--ink-teal);
    border: none; box-shadow: 0 0 24px rgba(255,255,255,0.6);
  }
  .btn-tenant { left: 214px; top: 212px; width: 231px; }
  .btn-maint { left: 214px; top: 330px; width: 277px; }
  .btn-work { left: 217px; top: 433px; width: 231px; }
  .btn-purchase { left: 217px; top: 550px; width: 231px; }
  .menu-btn {
    position: absolute; left: 218px; top: 671px; width: 63px; height: 62px;
    border-radius: 8px; background: #c5d8de;
    box-shadow: 4px 6px 12px rgba(40,80,95,0.3);
    display: flex; align-items: center; justify-content: center;
  }
  .topnav a {
    position: absolute; top: 164px; font-size: 12px; color: var(--ink-teal); text-decoration: none;
  }
  .search {
    position: absolute; left: 802px; top: 135px; width: 234px; height: 43px;
    background: #e6ebed; border-radius: 8px; padding: 10px 16px;
  }
  .rule { position: absolute; height: 1px; background: var(--line); }
  .calendar {
    position: absolute; left: 508px; top: 216px; width: 294px; height: 293px;
    border-radius: 14px;
    background: linear-gradient(180deg, var(--teal-light), var(--teal-dark));
    box-shadow: 8px 14px 28px rgba(74,135,153,0.35);
  }
  .weekdays { position: absolute; top: 34px; left: 14px; right: 14px; display: flex; }
  .weekdays span { width: 37px; text-align: center; font-size: 8px; color: var(--white); }
  .days {
    position: absolute; left: 19px; top: 64px;
    display: grid; grid-template-columns: repeat(7, 32px); column-gap: 5px; row-gap: 8px;
  }
  .days span {
    height: 36px; border-radius: 5px; background: var(--chip);
    font-size: 10px; display: flex; align-items: center; justify-content: center; color: var(--ink);
  }
  .name-tag {
    position: absolute; left: 861px; top: 216px; width: 94px; height: 29px;
    border-radius: 9px; background: linear-gradient(180deg, var(--teal), var(--teal-dark));
    color: var(--white); font-size: 11px; display: flex; align-items: center; justify-content: center;
  }
  .people { position: absolute; left: 861px; top: 269px; list-style: none; }
  .people li { display: flex; align-items: center; gap: 18px; height: 37px; margin-bottom: 18px; }
  .avatar { width: 34px; height: 37px; border-radius: 6px; background: #d6dadc; }
  .person-name { font-size: 11px; display: block; }
  .person-sub { font-size: 7px; color: var(--ink-teal); display: block; }
  .stats {
    position: absolute; left: 462px; top: 556px; width: 594px; height: 229px;
    border-radius: 8px; background: var(--panel);
  }
  .stats-title { position: absolute; left: 58px; top: 14px; font-size: 11px; }
  .gauge { position: absolute; top: 34px; width: 140px; text-align: center; }
  .gauge svg { width: 140px; height: 140px; display: block; }
  .gauge-label { font-size: 11px; color: var(--ink-teal); margin-top: 6px; }
</style>
</head>
<body>
  <aside class="sidebar"></aside>
  <div class="brand"><span class="brand-mark"></span>Nestora</div>

  <nav>
    <div class="dock-btn no-icon btn-tenant">Tenant Requests</div>
    <div class="dock-btn active btn-maint">
      <svg viewBox="0 0 40 28" fill="none" stroke="#3e7f8f" stroke-width="1.4" stroke-linecap="round">
        <path d="M10 4 L28 24 M28 4 L10 24"/><circle cx="9" cy="4" r="3"/><circle cx="29" cy="24" r="3"/>
      </svg>
      Maintenance
    </div>
    <div class="dock-btn btn-work">
      <svg viewBox="0 0 40 28" fill="none" stroke="#fff" stroke-width="1.3" stroke-linejoin="round">
        <path d="M10 6h16v14H10zM26 11h6l4 5v4H26z"/><circle cx="15" cy="22" r="2.5"/><circle cx="31" cy="22" r="2.5"/><path d="M2 12h6M4 16h5"/>
      </svg>
      Work order
    </div>
    <div class="dock-btn btn-purchase">
      <svg viewBox="0 0 40 28" fill="none" stroke="#fff" stroke-width="1.3" stroke-linejoin="round">
        <path d="M10 6h16v14H10zM26 11h6l4 5v4H26z"/><circle cx="15" cy="22" r="2.5"/><circle cx="31" cy="22" r="2.5"/><path d="M2 12h6M4 16h5"/>
      </svg>
      Purchase order
    </div>
    <div class="menu-btn">
      <svg width="34" height="24" viewBox="0 0 34 24" fill="#4a8799">
        <circle cx="3" cy="3" r="2.5"/><rect x="8" y="1" width="26" height="4" rx="2"/>
        <circle cx="3" cy="12" r="2.5"/><rect x="8" y="10" width="26" height="4" rx="2"/>
        <circle cx="3" cy="21" r="2.5"/><rect x="8" y="19" width="26" height="4" rx="2"/>
      </svg>
    </div>
  </nav>

  <header class="topnav">
    <a href="#" style="left:508px">Properties</a>
    <a href="#" style="left:617px">Tenant</a>
    <a href="#" style="left:722px">Contacts</a>
  </header>
  <div class="search">
    <svg width="22" height="22" viewBox="0 0 22 22" fill="none" stroke="#3e7f8f" stroke-width="2">
      <circle cx="8" cy="8" r="6"/><path d="M12.5 12.5 L20 20" stroke-linecap="round"/>
    </svg>
  </div>
  <div class="rule" style="left:508px; top:189px; width:548px"></div>

  <section class="calendar">
    <div class="weekdays">
      <span>SAT</span><span>SUN</span><span>MON</span><span>TUE</span><span>WED</span><span>THU</span><span>FRI</span>
    </div>
    <div class="days">
      <span>1</span><span>2</span><span>3</span><span>4</span><span>5</span><span>6</span><span>7</span>
      <span>1</span><span>2</span><span>3</span><span>4</span><span>5</span><span>6</span><span>7</span>
      <span>1</span><span>2</span><span>3</span><span>4</span><span>5</span><span>6</span><span>7</span>
      <span>1</span><span>2</span><span>3</span><span>4</span><span>5</span><span>6</span><span>7</span>
      <span></span><span></span>
    </div>
  </section>

  <div class="name-tag">Name</div>
  <div class="rule" style="left:861px; top:254px; width:195px"></div>
  <ul class="people">
    <li><span class="avatar"></span><div><span class="person-name">Name 01</span><span class="person-sub">Name 01 Name 01</span></div></li>
    <li><span class="avatar"></span><div><span class="person-name">Name 01 Name 01</span><span class="person-sub">Name 01 Name 01</span></div></li>
    <li><span class="avatar"></span><div><span class="person-name">Name 03 Name 03</span><span class="person-sub">Name 01 Name 01</span></div></li>
    <li><span class="avatar"></span><div><span class="person-name">Name 04 Name 04</span><span class="person-sub">Name 01 Name 01</span></div></li>
    <li><span class="avatar"></span><div><span class="person-name">Name 04 Name 04</span><span class="person-sub">Name 01 Name 01</span></div></li>
  </ul>
  <div class="rule" style="left:508px; top:540px; width:548px"></div>

  <section class="stats">
    <div class="stats-title">Properties</div>
    <div class="gauge" style="left:46px">
      <svg viewBox="0 0 140 140">
        <circle cx="70" cy="70" r="62" fill="none" stroke="#b9dcda" stroke-width="9"/>
        <circle cx="70" cy="70" r="62" fill="none" stroke="#5ea5aa" stroke-width="9" stroke-dasharray="311.6 389.6" transform="rotate(-90 70 70)"/>
        <text x="70" y="76" text-anchor="middle" font-size="16" fill="#3e7f8f" font-family="Source Sans 3, sans-serif">80%</text>
      </svg>
      <div class="gauge-label">Completed tenant request</div>
    </div>
    <div class="gauge" style="left:210px">
      <svg viewBox="0 0 140 140">
        <circle cx="70" cy="70" r="62" fill="none" stroke="#b9dcda" stroke-width="9"/>
        <circle cx="70" cy="70" r="62" fill="none" stroke="#5ea5aa" stroke-width="9" stroke-dasharray="272.7 389.6" transform="rotate(-90 70 70)"/>
        <text x="70" y="76" text-anchor="middle" font-size="16" fill="#3e7f8f" font-family="Source Sans 3, sans-serif">70%</text>
      </svg>
      <div class="gauge-label">Completed tenant request</div>
    </div>
    <div class="gauge" style="left:370px">
      <svg viewBox="0 0 140 140">
        <circle cx="70" cy="70" r="62" fill="none" stroke="#b9dcda" stroke-width="9"/>
        <circle cx="70" cy="70" r="62" fill="none" stroke="#5ea5aa" stroke-width="9" stroke-dasharray="214.3 389.6" transform="rotate(-90 70 70)"/>
        <text x="70" y="76" text-anchor="middle" font-size="16" fill="#3e7f8f" font-family="Source Sans 3, sans-serif">55%</text>
      </svg>
      <div class="gauge-label">Purchase orders</div>
    </div>
  </section>
</body>
</html>
```